Corvantel, LLC Website

Creating website for medical billing company.

Target Market(s)

Medical providers

Industry/Entity Type

Medical billing

Coding

Coded - Design and coding required

Number of Pages Required

3 page

Font styles to use
Other font styles liked:
• Fonts that match our logo.

Requirements
Must have
• First page (greeting and explanation of who we are). Second page something about me and company (I'll supply some content, make generic for now). And page three, information that people can give for us to contact them.
Nice to have
• A little animation. But not over-the-top. Colors that match our logo.
Should not have
• Over-the-top animation.

```html
<!DOCTYPE html>
<html lang="en">
<head>
<meta charset="utf-8">
<title>Corvantel, LLC — Medical Billing Services</title>
<link href="https://fonts.googleapis.com/css2?family=Fira+Sans:wght@400;500;600&family=Lato:wght@400;700&display=swap" rel="stylesheet">
<style>
:root{
  --navy:#17364c;
  --navy-deep:#122c3f;
  --cyan:#13a8cd;
  --ink:#1f2a33;
  --text:#5d6670;
  --light:#f4f5f6;
  --white:#ffffff;
  --footer:#1f2b34;
  --footer-line:#2c3943;
  --star:#f26a2e;
}
*{margin:0;padding:0;box-sizing:border-box}
html,body{width:1200px;height:4641px;overflow:hidden}
body{font-family:"Lato",sans-serif;color:var(--text);background:var(--white);position:relative}
h1,h2,h3,h4,.head{font-family:"Fira Sans",sans-serif;color:var(--ink);font-weight:500}
.abs{position:absolute}
.btn{display:inline-flex;align-items:center;justify-content:center;background:var(--cyan);color:#fff;font-family:"Fira Sans",sans-serif;font-weight:600;font-size:11px;letter-spacing:.5px;text-transform:uppercase}
.section-title{position:absolute;left:0;width:1200px;text-align:center;font-size:30px;font-weight:600}
.section-lead{position:absolute;left:50%;transform:translateX(-50%);width:520px;text-align:center;font-size:12.5px;line-height:22px}

/* header */
.site-header{position:absolute;top:0;left:0;width:1200px;height:81px;background:#fff;box-shadow:0 2px 6px rgba(0,0,0,.06)}
.topbar{position:absolute;top:0;left:395px;width:805px;height:32px;background:var(--navy);clip-path:polygon(2.5% 0,100% 0,100% 100%,0 100%);color:#fff;font-size:8.5px;display:flex;align-items:center}
.topbar .addr{margin-left:70px;display:flex;align-items:center;gap:6px}
.topbar .follow{margin-left:48px;display:flex;align-items:center;gap:6px}
.topbar .dot{width:6px;height:6px;border-radius:50%;background:#fff}
.topbar .quote{margin-left:40px;background:var(--cyan);padding:0 20px;height:18px;display:flex;align-items:center;font-size:8px}
.brand{position:absolute;left:118px;top:26px;display:flex;align-items:center;gap:8px;font-family:"Fira Sans",sans-serif;font-weight:500;font-size:17px;color:var(--navy)}
.brand .mark{width:14px;height:14px;background:var(--cyan)}
.nav{position:absolute;top:50px;left:404px;display:flex;gap:0;font-size:10.5px;color:var(--ink)}
.nav a{text-decoration:none;color:inherit;margin-right:50px}
.nav a.active{color:var(--navy);font-weight:700}

/* hero */
.hero{position:absolute;top:81px;left:0;width:1200px;height:632px;background:linear-gradient(100deg,#2f3a43 0%,#4a5660 45%,#8a949c 75%,#6c757c 100%)}
.hero .eyebrow{position:absolute;left:113px;top:190px;color:#e8ecef;font-size:12.5px;display:flex;align-items:center;gap:14px}
.hero .eyebrow span{width:46px;height:1px;background:#e8ecef}
.hero h1{position:absolute;left:113px;top:240px;color:#fff;font-size:43px;line-height:57px;font-weight:600;letter-spacing:.5px}
.hero p{position:absolute;left:113px;top:396px;width:440px;color:#e8ecef;font-size:12.5px;line-height:21px}
.hero .btn{position:absolute;left:113px;top:459px;width:192px;height:40px;font-size:11px;text-transform:none;font-weight:500}

/* services */
.services{position:absolute;top:713px;left:0;width:1200px;height:640px;background:var(--light)}
.svc-card{position:absolute;top:258px;width:232px;height:214px;background:#fff;box-shadow:0 2px 10px rgba(0,0,0,.06);text-align:center}
.svc-card.featured{background:var(--navy)}
.svc-card svg{margin-top:28px}
.svc-card h3{font-size:18px;font-weight:600;line-height:25px;margin-top:12px}
.svc-card p{font-size:12.5px;line-height:21px;margin:6px auto 0;width:180px}
.svc-card.featured h3{color:#fff}
.svc-card.featured p{color:#cfd8df}

/* unlock */
.unlock-band{position:absolute;top:1322px;left:281px;width:919px;height:467px;background:var(--navy)}
.unlock-photo{position:absolute;top:1384px;left:0;width:580px;height:450px;background:linear-gradient(120deg,#c8cfd4,#7e8a93 55%,#b3bcc2)}
.unlock-text{position:absolute;top:1413px;left:632px;width:445px;color:#d4dde3;font-size:12.5px;line-height:22px}
.unlock-text h2{color:#fff;font-size:30px;font-weight:500;margin-bottom:16px}
.unlock-text p{margin-bottom:12px}
.unlock-text .btn{width:172px;height:38px;margin-top:10px}

/* what we do */
.work{position:absolute;top:1865px;left:0;width:1200px;height:645px;background:var(--light)}
.work-card{position:absolute;top:198px;width:319px;height:380px}
.work-card .photo{width:319px;height:236px}
.work-card .box{position:absolute;left:18px;top:177px;width:284px;height:201px;background:#fff;box-shadow:0 2px 10px rgba(0,0,0,.08);padding:22px 40px 0 40px}
.work-card .box h3{font-size:21px;font-weight:500;margin-bottom:8px}
.work-card .box p{font-size:12px;line-height:22px}
.work-card .box a{display:block;margin-top:6px;font-size:10px;font-weight:700;color:var(--cyan);text-decoration:none;letter-spacing:.4px}
.work-card.featured .box{background:var(--navy)}
.work-card.featured .box h3{color:#fff}
.work-card.featured .box p{color:#cfd8df}
.work-card.featured .box a{color:#fff}

/* consult */
.consult{position:absolute;top:2510px;left:0;width:1200px;height:297px;background:linear-gradient(90deg,#3b5774,#4e6d8c 50%,#3e5a76);text-align:center;color:#fff}
.consult .phone{position:absolute;top:43px;left:0;width:1200px;display:flex;justify-content:center;align-items:center;gap:12px;font-family:"Fira Sans",sans-serif;font-size:22px;font-weight:500}
.consult h2{position:absolute;top:85px;width:1200px;color:#fff;font-size:30px;font-weight:600}
.consult p{position:absolute;top:144px;left:50%;transform:translateX(-50%);width:480px;font-size:12.5px;line-height:22px;color:#e3e9ef}
.consult .outline{position:absolute;top:211px;left:518px;width:172px;height:40px;border:1px solid #fff;display:flex;align-items:center;justify-content:center;font-family:"Fira Sans",sans-serif;font-size:11px;font-weight:600;letter-spacing:.5px}

/* testimonials */
.testi-card{position:absolute;top:3041px;width:496px;height:256px;background:var(--light)}
.testi-card .rule{position:absolute;left:62px;top:42px;width:1px;height:172px;background:var(--ink)}
.testi-card .quote{position:absolute;left:38px;top:104px;width:50px;height:50px;border-radius:50%;background:#fff;border:3px solid var(--cyan);display:flex;align-items:center;justify-content:center}
.testi-card .quote i{width:36px;height:36px;border-radius:50%;background:var(--cyan);color:#fff;font-style:normal;font-family:"Fira Sans",sans-serif;font-weight:600;font-size:20px;display:flex;align-items:center;justify-content:center}
.testi-card .stars{position:absolute;left:115px;top:36px;color:var(--star);font-size:14px;letter-spacing:5px}
.testi-card p{position:absolute;left:115px;top:80px;width:340px;font-size:12.5px;line-height:22px}
.testi-card h4{position:absolute;left:115px;top:166px;font-size:17px;font-weight:500}
.testi-card .loc{position:absolute;left:115px;top:191px;font-size:11.5px}
.testi-card .avatar{position:absolute;left:400px;top:165px;width:58px;height:58px;border-radius:50%;background:linear-gradient(135deg,#8e9aa4,#5b6770)}
.dots{position:absolute;top:3341px;left:563px;display:flex;gap:10px}
.dots span{width:9px;height:9px;border-radius:50%;background:#d8dcdf}
.dots span.on{background:#fff;border:2px solid var(--star)}

/* contact */
.contact{position:absolute;top:3388px;left:4px;width:1196px;height:802px;background:var(--light)}
.contact-box{position:absolute;top:3598px;left:94px;width:1009px;height:456px;background:#fff}
.contact-info{position:absolute;left:0;top:0;width:508px;height:456px;background:var(--navy);color:#fff;padding:62px 0 0 86px;font-size:11.5px;line-height:17px}
.contact-info .label{font-family:"Fira Sans",sans-serif;font-weight:500;font-size:15px;margin-bottom:22px}
.contact-info .call{font-family:"Fira Sans",sans-serif;font-size:20px;margin-bottom:8px}
.contact-info .grp{margin-top:22px}
.contact-info b{font-weight:700}
.socials{display:flex;gap:10px;margin-top:50px}
.socials span{width:30px;height:30px;border-radius:50%;background:#5a6f80}
.socials span.on{background:#fff}
.contact-form{position:absolute;left:594px;top:56px;width:330px}
.contact-form h3{font-family:"Fira Sans",sans-serif;color:var(--navy);font-size:16px;font-weight:500;margin-bottom:22px}
.field{height:32px;background:var(--light);margin-bottom:17px;font-size:9px;color:#8a929a;padding:10px 14px}
.field.msg{height:94px}
.contact-form .btn{width:108px;height:36px;margin-top:2px}

/* info strip */
.strip{position:absolute;top:4140px;left:63px;width:1070px;height:103px;background:var(--cyan);border-radius:6px;color:#fff;z-index:2}
.strip .item{position:absolute;top:0;height:103px;display:flex;align-items:center;gap:18px}
.strip h4{color:#fff;font-size:17px;font-weight:500;margin-bottom:6px}
.strip small{font-size:11.5px}
.strip .chev{position:absolute;top:0}

/* footer */
.site-footer{position:absolute;top:4190px;left:0;width:1200px;height:451px;background:var(--footer);color:#c9d1d8}
.fcol{position:absolute;top:136px}
.fcol h4{color:#fff;font-size:17px;font-weight:500;margin-bottom:30px}
.fcol p{font-size:12px;line-height:30px}
.fcol a{color:#c9d1d8;font-size:12px;display:block;line-height:31px}
.fcol .more{color:var(--cyan);font-size:14px;margin-top:10px}
.news{display:flex;margin-top:18px}
.news .in{width:278px;height:54px;background:#fff;color:#333;font-size:12px;padding:18px 16px}
.news .go{width:62px;height:54px;background:var(--cyan);display:flex;align-items:center;justify-content:center}
.fbar{position:absolute;left:0;top:386px;width:1200px;height:1px;background:var(--footer-line)}
.flogo{position:absolute;left:63px;top:386px;width:173px;height:65px;background:var(--cyan);display:flex;align-items:center;justify-content:center;gap:6px;color:#fff;font-family:"Fira Sans",sans-serif;font-size:13px;font-weight:500}
.flogo i{width:10px;height:10px;background:#fff}
.fsocial{position:absolute;right:0;top:386px;display:flex}
.fsocial span{width:59px;height:65px;border-left:1px solid var(--footer-line);display:flex;align-items:center;justify-content:center}
.fsocial span::after{content:"";width:10px;height:10px;border-radius:50%;background:#46525c}
</style>
</head>
<body>

<header class="site-header">
  <div class="topbar">
    <div class="addr"><svg width="7" height="9" viewBox="0 0 10 13"><path d="M5 0a5 5 0 0 0-5 5c0 4 5 8 5 8s5-4 5-8a5 5 0 0 0-5-5zm0 7a2 2 0 1 1 0-4 2 2 0 0 1 0 4z" fill="#fff"/></svg>48 Harlow St., Brookfield, NY 10542</div>
    <div class="follow">Follow Us: <span class="dot"></span><span class="dot"></span><span class="dot"></span></div>
    <div class="quote">GET QUOTATION</div>
  </div>
  <div class="brand"><span class="mark"></span>Corvantel, LLC</div>
  <nav class="nav">
    <a class="active">Home</a><a>About Us</a><a>Services</a><a>Team</a><a>Gallery</a><a>Solutions</a><a>Contact Us</a>
  </nav>
</header>

<section class="hero" role="img" aria-label="Office photo of colleagues working together at a shared desk">
  <div class="eyebrow">On the other hand <span></span></div>
  <h1>Empowering Healthcare<br>Providers, Boosting Revenue</h1>
  <p>Lorem ipsum dolor sit amet, consectetur adipiscing elit, sed do eiusmod tempor incididunt ut labore et dolore magna</p>
  <div class="btn">Discover more</div>
</section>

<section class="services">
  <h2 class="section-title" style="top:130px">Leading Medical Billing Services</h2>
  <p class="section-lead" style="top:182px">Lorem ipsum dolor sit amet, consectetur adipiscing elit, sed do eiusmod tempor incididunt ut labore et dolore magna aliqua. Ut enim ad min</p>

  <div class="svc-card" style="left:90px">
    <svg width="44" height="44" viewBox="0 0 44 44" fill="none" stroke="#17364c" stroke-width="1.6"><circle cx="22" cy="22" r="14"/><circle cx="22" cy="22" r="7"/><path d="M22 2v10M22 32v10M2 22h10M32 22h10"/></svg>
    <h3>Client<br>Centric</h3>
    <p>Lorem ipsum dolor sit amet, consectetur adipiscing</p>
  </div>
  <div class="svc-card featured" style="left:350px">
    <svg width="44" height="44" viewBox="0 0 44 44" fill="none" stroke="#fff" stroke-width="1.6"><circle cx="22" cy="13" r="6"/><circle cx="10" cy="17" r="4"/><circle cx="34" cy="17" r="4"/><path d="M12 38v-6a10 10 0 0 1 20 0v6zM3 34v-4a7 7 0 0 1 9-6M41 34v-4a7 7 0 0 0-9-6"/></svg>
    <h3>Quality<br>Workmanship</h3>
    <p>Lorem ipsum dolor sit amet, consectetur adipiscing</p>
  </div>
  <div class="svc-card" style="left:608px">
    <svg width="44" height="44" viewBox="0 0 44 44" fill="none" stroke="#17364c" stroke-width="1.6"><path d="M8 38h26M14 32h14M20 6l10 6-6 10-10-6zM20 22l-4 10M30 16a8 8 0 0 1-2 16"/></svg>
    <h3>Competitive<br>Pricing</h3>
    <p>Lorem ipsum dolor sit amet, consectetur adipiscing</p>
  </div>
  <div class="svc-card" style="left:870px">
    <svg width="44" height="44" viewBox="0 0 44 44" fill="none" stroke="#17364c" stroke-width="1.6"><path d="M22 6l14 10-5 18H13L8 16z"/><circle cx="22" cy="6" r="3" fill="#fff"/><circle cx="36" cy="16" r="3" fill="#fff"/><circle cx="31" cy="34" r="3" fill="#fff"/><circle cx="13" cy="34" r="3" fill="#fff"/><circle cx="8" cy="16" r="3" fill="#fff"/></svg>
    <h3>Expertise and<br>Experience</h3>
    <p>Lorem ipsum dolor sit amet, consectetur adipiscing</p>
  </div>

  <div class="btn abs" style="left:519px;top:512px;width:172px;height:41px">Learn more about</div>
</section>

<div class="unlock-band"></div>
<div class="unlock-photo" role="img" aria-label="Photo of two businessmen reviewing a tablet at an office desk"></div>
<div class="unlock-text">
  <h2>Unlock Your Earnings</h2>
  <p>Lorem ipsum dolor sit amet, consectetur adipiscing elit, sed do eiusmod tempor incididunt ut labore et dolore magna aliqua. Ut enim ad minim veniam, quis nostrud ex</p>
  <p>Lorem ipsum dolor sit amet, consectetur adipiscing elit, sed do eiusmod tempor incididunt ut labore et dolore magna aliqua. Ut enim ad minim veniam, quis nostrud exercitation ullamco laboris nisi ut aliquip ex ea commodo consequat. Duis aute iru</p>
  <div class="btn">Learn more about</div>
</div>

<section class="work">
  <h2 class="section-title" style="top:50px">What We Do</h2>
  <p class="section-lead" style="top:100px">Lorem ipsum dolor sit amet, consectetur adipiscing elit, sed do eiusmod tempor incididunt ut labore et dolore magna aliqua. Ut enim ad min</p>

  <div class="work-card" style="left:94px">
    <div class="photo" role="img" aria-label="Photo of a smiling billing specialist in an office" style="background:linear-gradient(135deg,#c3ccd2,#7d8a94)"></div>
    <div class="box"><h3>Patient Billing</h3><p>Lorem ipsum dolor sit amet, consectetur adipiscing elit, sed do eiusmod tempor incididunt ut labore et dolore magna aliqua.</p><a>LEARN MORE</a></div>
  </div>
  <div class="work-card featured" style="left:440px">
    <div class="photo" role="img" aria-label="Photo of analysts reviewing figures on a laptop" style="background:linear-gradient(135deg,#4d4f52,#25282b)"></div>
    <div class="box"><h3>Financial Analysis</h3><p>Lorem ipsum dolor sit amet, consectetur adipiscing elit, sed do eiusmod tempor incididunt ut labore et dolore magna aliqua.</p><a>LEARN MORE</a></div>
  </div>
  <div class="work-card" style="left:787px">
    <div class="photo" role="img" aria-label="Photo of auditors discussing documents at a table" style="background:linear-gradient(135deg,#d5dadd,#808a92)"></div>
    <div class="box"><h3>Auditing Services</h3><p>Lorem ipsum dolor sit amet, consectetur adipiscing elit, sed do eiusmod tempor incididunt ut labore et dolore magna aliqua.</p><a>LEARN MORE</a></div>
  </div>
</section>

<section class="consult" role="img" aria-label="Blue-toned photo of a team meeting in a bright office">
  <div class="phone"><svg width="32" height="32" viewBox="0 0 24 24" fill="none" stroke="#fff" stroke-width="1.4"><path d="M5 3h4l2 5-2.5 1.5a11 11 0 0 0 6 6L16 13l5 2v4a2 2 0 0 1-2 2A16 16 0 0 1 3 5a2 2 0 0 1 2-2z"/></svg>555-210-4478</div>
  <h2>Get Free Consultation Today</h2>
  <p>Lorem ipsum dolor sit amet, consectetur adipiscing elit, sed do eiusmod tempor incididunt ut labore et dolore magna aliqua.</p>
  <div class="outline">CONTACT US NOW</div>
</section>

<h2 class="section-title" style="top:2893px">Client Testimonials</h2>
<p class="section-lead" style="top:2948px">Lorem ipsum dolor sit amet, consectetur adipiscing elit, sed do eiusmod tempor incididunt ut labore et dolore magna aliqua. Ut enim ad min</p>

<div class="testi-card" style="left:88px">
  <div class="rule"></div><div class="quote"><i>”</i></div>
  <div class="stars">★★★★★</div>
  <p>Lorem ipsum dolor sit amet, consectetur adipiscing elit, sed do eiusmod tempor incididunt ut labore et dolore magna aliqua. Ut enim</p>
  <h4>Marla Dene</h4><div class="loc">Pine Hollow</div>
  <div class="avatar" role="img" aria-label="Client portrait photo"></div>
</div>
<div class="testi-card" style="left:609px">
  <div class="rule"></div><div class="quote"><i>”</i></div>
  <div class="stars">★★★★★</div>
  <p>Lorem ipsum dolor sit amet, consectetur adipiscing elit, sed do eiusmod tempor incididunt ut labore et dolore magna aliqua. Ut enim</p>
  <h4>Marla Dene</h4><div class="loc">Pine Hollow</div>
  <div class="avatar" role="img" aria-label="Client portrait photo" style="background:linear-gradient(135deg,#e2d6c8,#a89684)"></div>
</div>
<div class="dots"><span></span><span></span><span class="on"></span><span></span></div>

<section class="contact">
  <h2 class="section-title" style="top:56px;left:-4px">Contact Us</h2>
  <p class="section-lead" style="top:108px">Lorem ipsum dolor sit amet, consectetur adipiscing elit, sed do eiusmod tempor incididunt ut labore et dolore magna aliqua. Ut enim ad min</p>
</section>

<div class="contact-box">
  <div class="contact-info">
    <div class="label">CONTACT US</div>
    <div class="call">Call: 555-0148</div>
    <div>hello@corvantel.com</div>
    <div class="grp"><b>Address:</b><br>ELM COURT<br>2204 Ridge Road</div>
    <div class="grp"><b>Operating Hours</b><br>Monday to Saturday: 9:00 - 18:00<br>Sunday: Closed</div>
    <div class="socials"><span></span><span class="on"></span><span></span><span></span></div>
  </div>
  <div class="contact-form">
    <h3>FREE CONSULTATION</h3>
    <div class="field">Your Name</div>
    <div class="field">Email</div>
    <div class="field">Phone</div>
    <div class="field msg">Message ...</div>
    <div class="btn">Submit</div>
  </div>
</div>

<div class="strip">
  <div class="item" style="left:40px">
    <svg width="52" height="46" viewBox="0 0 52 46" fill="none" stroke="#fff" stroke-width="1.6"><path d="M26 4a10 10 0 0 0-10 10c0 8 10 18 10 18s10-10 10-18A10 10 0 0 0 26 4z"/><circle cx="26" cy="14" r="4"/><path d="M14 28L3 42h46L38 28"/></svg>
    <div><h4>Address</h4><small>72 Ridge Road, Denver, USA</small></div>
  </div>
  <svg class="chev" style="left:345px" width="22" height="103" viewBox="0 0 22 103" fill="none" stroke="#fff" stroke-width="1.4"><path d="M2 0l18 51L2 103"/></svg>
  <div class="item" style="left:400px">
    <svg width="48" height="48" viewBox="0 0 24 24" fill="none" stroke="#fff" stroke-width="1"><path d="M5 3h4l2 5-2.5 1.5a11 11 0 0 0 6 6L16 13l5 2v4a2 2 0 0 1-2 2A16 16 0 0 1 3 5a2 2 0 0 1 2-2z"/></svg>
    <div><h4>Phone</h4><small>+1 555 019 3321</small></div>
  </div>
  <svg class="chev" style="left:702px" width="22" height="103" viewBox="0 0 22 103" fill="none" stroke="#fff" stroke-width="1.4"><path d="M2 0l18 51L2 103"/></svg>
  <div class="item" style="left:755px">
    <svg width="48" height="48" viewBox="0 0 48 48" fill="none" stroke="#fff" stroke-width="1.6"><path d="M4 20l20-14 20 14v24H4z"/><path d="M4 20l20 14 20-14"/><rect x="12" y="10" width="24" height="16"/></svg>
    <div><h4>Email Contact</h4><small>hello@corvantel.com</small></div>
  </div>
</div>

<footer class="site-footer">
  <div class="fcol" style="left:65px;width:300px">
    <h4>About Corvantel</h4>
    <p>Lorem ipsum dolor sit amet, consectetur adipi elit, sed do eiusmod tempor incididunt ut lab dolore magna aliqua.</p>
    <a class="more"><u>Read More</u></a>
  </div>
  <div class="fcol" style="left:432px">
    <h4>Useful Links</h4>
    <div style="display:flex;gap:76px">
      <div><a><u>About Us</u></a><a><u>Projects</u></a><a><u>Blog</u></a><a><u>Contact Us</u></a></div>
      <div><a><u>Services</u></a><a><u>Shop</u></a><a><u>Privacy Policy</u></a><a><u>Help Desk</u></a></div>
    </div>
  </div>
  <div class="fcol" style="left:795px;width:340px">
    <h4>Useful Links</h4>
    <p style="line-height:22px;font-size:13px">If you have any questions, Subscribe to our newsletter to get our latest products</p>
    <div class="news"><div class="in">Email</div><div class="go"><svg width="22" height="18" viewBox="0 0 22 18" fill="none" stroke="#fff" stroke-width="1.6"><path d="M1 9h19M12 1l8 8-8 8"/></svg></div></div>
  </div>
  <div class="fbar"></div>
  <div class="flogo"><i></i>Corvantel, LLC</div>
  <div class="fsocial"><span></span><span></span><span></span><span></span></div>
</footer>

</body>
</html>
```